Calder Ridge Minerals

Looking for a cool, glossy business card...white with our logo on one side and then the a smaller version of the logo on the other side (top left hand corner) and then the name and position of the person next to it, and then the office address and email address on the bottom left hand corner and the phone numbers & email address on the bottom right hand corner. I have the logo already...can pass it on when you're ready.

```html
<!DOCTYPE html>
<html lang="en">
<head>
<meta charset="utf-8">
<title>Calder Ridge Minerals – Business Card</title>
<link rel="stylesheet" href="https://fonts.googleapis.com/css2?family=Cinzel:wght@400;600&family=Archivo+Narrow:wght@400&family=Montserrat:wght@500&display=swap">
<style>
  :root {
    --backdrop: #e6e3de;
    --card: #ffffff;
    --ink: #2f2f36;
    --brand-grey: #3b3b44;
    --brand-blue: #2c3f9c;
    --brand-red: #c7202b;
    --rule: #9a9a9a;
  }
  * { margin: 0; padding: 0; box-sizing: border-box; }
  html, body { width: 900px; height: 1200px; overflow: hidden; }
  body { background: var(--backdrop); position: relative; font-family: "Archivo Narrow", "Arial Narrow", sans-serif; color: var(--ink); }

  .card {
    position: absolute; left: 80px; width: 733px; height: 429px;
    background: var(--card); border-radius: 28px;
    box-shadow: 0 6px 16px rgba(0,0,0,.25);
  }
  .card--front { top: 128px; }
  .card--back {
    top: 645px;
    display: flex; align-items: center; justify-content: center;
  }

  .brand-name {
    font-family: "Cinzel", Georgia, serif; font-weight: 600;
    color: var(--brand-grey); text-align: center; line-height: 1.1;
  }
  .card--front .brand-name {
    position: absolute; left: 24px; top: 96px; width: 218px; font-size: 22px;
  }
  .card--back .brand-name { font-size: 44px; }
  .brand-name .line-small { display: block; font-size: .62em; letter-spacing: .3em; }

  .divider {
    position: absolute; left: 264px; top: 40px; width: 1.5px; height: 157px; background: var(--rule);
  }
  .person { position: absolute; left: 292px; top: 88px; }
  .person__name {
    font-family: "Cinzel", Georgia, serif; font-weight: 600; font-size: 27px; color: var(--ink);
    letter-spacing: .01em;
  }
  .person__role {
    font-family: "Montserrat", sans-serif; font-weight: 500; font-size: 15px;
    color: var(--brand-blue); letter-spacing: .2em; margin-top: 2px;
  }

  .contact { position: absolute; top: 321px; list-style: none; font-size: 17.5px; }
  .contact li { display: flex; align-items: center; gap: 9px; height: 29px; }
  .contact--left { left: 30px; }
  .contact--right { right: 32px; }
  .contact--right li { justify-content: flex-end; }
  .icon { width: 18px; height: 18px; flex: none; }
</style>
</head>
<body>
  <section class="card card--front" aria-label="Card front">
    <div class="brand-name">Calder Ridge <span class="line-small">Minerals</span></div>
    <div class="divider"></div>
    <div class="person">
      <div class="person__name">Daniel Hayes</div>
      <div class="person__role">MANAGING DIRECTOR</div>
    </div>

    <ul class="contact contact--left">
      <li>
        <svg class="icon" viewBox="0 0 18 18" aria-hidden="true"><path d="M9 1a6 6 0 0 0-6 6c0 4.5 6 10 6 10s6-5.5 6-10a6 6 0 0 0-6-6z" fill="var(--brand-blue)"/><circle cx="9" cy="7" r="2.3" fill="#fff"/></svg>
        218 W. Linden Ave Suite B, Marlow, FL 33602
      </li>
      <li>
        <svg class="icon" viewBox="0 0 18 18" aria-hidden="true"><rect x="1" y="4" width="16" height="11" fill="var(--brand-red)"/><path d="M1 4l8 6 8-6" fill="none" stroke="#fff" stroke-width="1.4"/></svg>
        Info@calderridgeminerals.com
      </li>
    </ul>

    <ul class="contact contact--right">
      <li>
        813-555-0142
        <svg class="icon" viewBox="0 0 18 18" aria-hidden="true"><path d="M4 2l3 3-1.6 2.2a10 10 0 0 0 5.4 5.4L13 11l3 3-2 2.5C7.5 16 2 10.5 1.5 4z" fill="var(--brand-red)"/></svg>
      </li>
      <li>
        www.calderridgeminerals.com
        <svg class="icon" viewBox="0 0 18 18" aria-hidden="true"><g fill="none" stroke="var(--brand-blue)" stroke-width="1.4"><circle cx="9" cy="9" r="7.5"/><ellipse cx="9" cy="9" rx="3.3" ry="7.5"/><path d="M1.5 9h15M3 5h12M3 13h12"/></g></svg>
      </li>
    </ul>
  </section>

  <section class="card card--back" aria-label="Card back">
    <div class="brand-name">Calder Ridge <span class="line-small">Minerals</span></div>
  </section>
</body>
</html>
```